Web Design Project for Film Business

We need a web design for a new company based in Bondi Beach, Sydney, Australia. We basically provide filming and video editing services. Our targets are basically corporate videos, wedding videos and other types of functions.
The important thing to know about us is that we are not just people that press the record button, we consider ourselves story tellers. We can make something boring like a conference look interesting to watch and we can also make a wedding look like a blockbuster movie that you can't look away from until its finished.
We need something as new and fresh as Bondi Beach. A young place where people come from all over the world to enjoy summer and we are lucky to be based here.
To see some of our work please visit our tavlora Channel. Make sure you watch a couple of wedding video and the corporate video so you can have a better understanding about our style.
Please note- we are not trying to market ourselves exclusively as wedding videographers, nor do we want to exploit the idea of the beach.

http://tavlora.com/channels/815374

sites that we really like:

http://www.quillpathreels.co.uk/
http://www.marnowebb.co.uk/

Target Market(s)

Couples - Corporate

Industry/Entity Type

Business

Requirements
Must have
• 5 to 6 pages (we are still deciding)
-main page
-our story (story about Karrow Films)
-your story (page designated for wedding videos)
-your business (page designated for corporate videos)
-contact us
-other stuff
Nice to have
• I would like to see some animation. Maybe you can animate our logo. Up to the designer

```html
<!DOCTYPE html>
<html lang="en">
<head>
<meta charset="utf-8">
<title>Karrow Films</title>
<link rel="stylesheet" href="https://fonts.googleapis.com/css2?family=Bebas+Neue&family=Oswald:wght@300;400;500&family=Russo+One&family=Open+Sans:ital,wght@0,400;0,600;1,400&family=Gelasio:ital@1&display=swap">
<style>
:root{
  --bg:#1d1d1d;
  --bg-lower:#232323;
  --panel:#121212;
  --ink:#f2f2f2;
  --muted:#8a8a8a;
  --dim:#5a5a5a;
  --logo:#3c3c3c;
  --cyan:#35cdd6;
  --red:#d8213c;
  --gold:#e6a232;
  --tan:#a38d6b;
  --rule:#333;
}
*{margin:0;padding:0;box-sizing:border-box}
html,body{width:1000px;height:1200px;overflow:hidden;background:var(--bg)}
body{position:relative;font-family:"Open Sans",Verdana,sans-serif;color:var(--ink)}
.abs{position:absolute}
.glow{left:0;top:190px;width:1000px;height:330px;
  background:radial-gradient(ellipse 120px 170px at 0 50%,rgba(190,110,20,.55),transparent),
             radial-gradient(ellipse 120px 170px at 100% 50%,rgba(190,110,20,.55),transparent)}
.logo{left:72px;top:22px;font-family:"Bebas Neue",sans-serif;font-size:42px;line-height:34px;color:var(--logo)}
.nav{left:343px;top:30px;width:587px;height:62px;border:1px solid #3d3d3d;border-radius:3px;
  background:linear-gradient(#2e2e2e,#1a1a1a);box-shadow:0 2px 6px #000;display:flex;align-items:center;padding-left:23px;gap:0}
.nav a{font-family:"Oswald",sans-serif;font-weight:500;font-size:17px;color:var(--ink);text-decoration:none;padding:4px 7px;margin-right:16px;letter-spacing:.3px}
.nav a.current{background:#101010;border-radius:2px}
.tab{left:749px;top:95px;width:90px;height:23px;background:var(--red);border-radius:0 0 4px 4px;
  font-style:italic;font-size:12px;text-align:center;line-height:22px}
.hero{left:68px;top:135px;width:866px;height:365px;border-radius:4px;
  background:linear-gradient(90deg,#3a2a1c 0%,#5a4030 30%,#2b1f18 52%,#6a5344 62%,#24201e 78%,#8a7a6e 100%)}
.hero-caption{left:585px;top:432px;font-family:"Oswald",sans-serif;font-weight:300;color:#c9c4bd}
.hero-caption b{display:block;font-weight:300;font-size:14px;letter-spacing:.5px}
.hero-caption span{display:block;font-size:12px;color:#a59f98;margin-left:16px}
.ribbon{height:36px;background:#2e2e2e;clip-path:polygon(0 20%,6% 0,100% 8%,96% 100%,2% 92%);
  font-family:"Oswald",sans-serif;font-weight:300;font-size:17px;color:#cfcfcf;padding:7px 0 0 22px}
.thumb{width:155px;height:120px;background:#3a3a3a;padding:5px;box-shadow:0 2px 6px #000}
.thumb div{width:100%;height:100%}
.card-title{font-size:11.5px;color:var(--cyan)}
.card-by{font-size:10px;color:var(--muted);margin-bottom:10px}
.card-list{list-style:none;width:155px}
.card-list li{font-size:9.5px;color:var(--muted);border-bottom:1px solid #2c2c2c;height:16px;line-height:15px}
.card-more{font-size:9.5px;color:var(--muted);margin-top:9px}
.card-more b{color:#ddd;font-weight:600}
.welcome{left:548px;top:556px;width:374px}
.welcome h2{font-family:"Oswald",sans-serif;font-weight:300;font-size:26px;line-height:28px;color:#bdbdbd}
.welcome h3{font-family:"Bebas Neue",sans-serif;font-size:32px;line-height:28px;color:var(--tan);letter-spacing:.5px;border-bottom:1px solid var(--rule);padding-bottom:12px}
.welcome p{font-size:9.3px;line-height:14.3px;color:var(--muted);margin:10px 0 0 3px}
.welcome .card-more{margin:17px 0 0 3px}
.divider{left:0;top:870px;width:1000px;height:290px;background:var(--bg-lower);border-top:1px solid #2d2d2d}
.brush{background:var(--panel);clip-path:polygon(0 12%,4% 0,40% 6%,70% 0,100% 10%,98% 55%,100% 92%,60% 100%,30% 94%,3% 100%,1% 55%)}
.question{left:55px;top:885px;width:222px;height:65px;font-family:"Russo One",sans-serif;font-size:25px;color:var(--cyan);padding:21px 0 0 20px;letter-spacing:1px}
.contact{left:145px;top:940px;width:340px;height:56px;display:flex;padding:9px 0 0 18px;gap:35px}
.contact small{display:block;font-size:10.5px;color:#eee}
.contact strong{display:block;font-weight:400;font-size:16px;color:var(--cyan)}
.social{width:122px;height:26px;background:var(--red);font-family:"Russo One",sans-serif;font-size:12.5px;color:#fff;display:flex;align-items:center;gap:6px;padding-left:12px;
  clip-path:polygon(0 15%,8% 0,100% 10%,96% 50%,100% 92%,5% 100%,2% 55%)}
.social i{width:14px;height:14px;background:#fff;border-radius:2px;display:block}
.social.right{flex-direction:row-reverse;justify-content:flex-end;padding-left:18px}
.share{left:200px;top:1040px;width:145px;height:66px;font-family:"Russo One",sans-serif;font-size:15px;line-height:17px;color:var(--red);padding:15px 0 0 28px}
.happy{left:565px;top:893px;width:300px;height:48px;font-size:16px;color:var(--gold);text-align:center;line-height:46px}
.quote-line{left:535px;top:916px;width:360px;height:1px;background:#3a3a3a}
.quote{left:581px;top:964px;width:312px;font-family:"Gelasio",Georgia,serif;font-style:italic;font-size:13.3px;line-height:16.3px;color:#777}
.mark{font-family:Georgia,serif;font-size:90px;color:#3a3a3a;line-height:1}
.footer{left:0;top:1158px;width:1000px;height:42px;background:#151515;border-top:1px solid #2c2c2c}
.footer .flogo{position:absolute;left:703px;top:6px;font-family:"Bebas Neue",sans-serif;font-size:17px;line-height:14px;color:#474747}
.footer p{position:absolute;left:762px;top:13px;font-size:9.5px;color:#5e5e5e}
</style>
</head>
<body>
<div class="abs glow"></div>

<header>
  <div class="abs logo">Karrow<br>Films</div>
  <nav class="abs nav">
    <a class="current" href="#">HOME</a><a href="#">WHO</a><a href="#">BLOG</a><a href="#">PORTFOLIO</a><a href="#">PHOTOS</a><a href="#">PROJECTS</a><a href="#">CONTACT</a>
  </nav>
  <div class="abs tab">Freah</div>
</header>

<section>
  <div class="abs hero" role="img" aria-label="Wedding film still: bride and groom in a cathedral"></div>
  <div class="abs hero-caption"><b>LIAM+SOPHIA</b><span>by Rafael Monte</span></div>
</section>

<section>
  <div class="abs ribbon" style="left:65px;top:558px;width:215px">FRESH PROJECTS</div>
  <div class="abs thumb" style="left:88px;top:605px"><div role="img" aria-label="Project still: couple on a seaside promenade" style="background:linear-gradient(#c9d2da,#8a9aa6 55%,#6f8190)"></div></div>
  <div class="abs" style="left:89px;top:739px">
    <div class="card-title">Noah+Elena</div>
    <div class="card-by">by Rafael Monte</div>
    <ul class="card-list"><li>Lorem ipsum dolor</li><li>Lorem ipsum dolor</li><li>Lorem ipsum dolor</li><li>Lorem ipsum dolor</li></ul>
    <div class="card-more">See <b>Project</b> +</div>
  </div>

  <div class="abs ribbon" style="left:308px;top:558px;width:217px">LATEST WORK</div>
  <div class="abs thumb" style="left:340px;top:605px"><div role="img" aria-label="Conference still: speaker on stage" style="background:radial-gradient(circle at 45% 50%,#4a4f66,#1c1f3a 70%)"></div></div>
  <div class="abs" style="left:341px;top:739px">
    <div class="card-title">Harlow National Con</div>
    <div class="card-by">by Rafael Monte</div>
    <ul class="card-list"><li>Lorem ipsum dolor</li><li>Lorem ipsum dolor</li><li>Lorem ipsum dolor</li><li>Lorem ipsum dolor</li></ul>
    <div class="card-more">See <b>Portfolio</b> +</div>
  </div>

  <article class="abs welcome">
    <h2>WELCOME TO</h2>
    <h3>KARROW FILMS</h3>
    <p>Lorem ipsum dolor sit amet, consectetur adipisicing elit, sed do eiusmod tempor incididunt ut labore et dolore magna aliqua. Ut enim ad minim veniam, quis nostrud exercitation ullamco laboris nisi ut aliquip ex ea commodo consequat. Duis aute irure dolor in reprehenderit in voluptate velit esse cillum dolore eu fugiat nulla pariatur. Excepteur sint occaecat cupidatat non proident, sunt in culpa qui officia deserunt mollit anim id est laborum. Lorem ipsum dolor sit amet, consectetur adipisicing elit, sed do eiusmod tempor incididunt ut labore et dolore magna aliqua. Ut enim ad minim veniam, quis nostrud exercitation ullamco laboris nisi ut aliquip ex ea commodo consequat. Duis aute irure dolor in reprehenderit in voluptate velit esse cillum dolore eu fugiat nulla pariatur. Excepteur sint occaecat cupidatat non proident, sunt in culpa qui officia deserunt mollit anim id est laborum. fugiat nulla pariatur. Excepteur sint occaecat cupidatat non proident, sunt in culpa qui officia deserunt mollit anim id est laborum.</p>
    <div class="card-more">Read <b>More</b> +</div>
  </article>
</section>

<section class="abs divider"></section>

<section>
  <div class="abs brush question">QUESTION?</div>
  <div class="abs brush contact">
    <div><small>Call us</small><strong>1-888-402-7316</strong></div>
    <div><small>Email us</small><strong>info@karrowfilms.com</strong></div>
  </div>

  <div class="abs social" style="left:92px;top:1031px;transform:rotate(3deg)"><i></i>Warbler</div>
  <div class="abs social" style="left:94px;top:1064px;transform:rotate(-2deg)"><i></i>Pagewall</div>
  <div class="abs social" style="left:98px;top:1097px;transform:rotate(-5deg)"><i></i>Snapgrid</div>
  <div class="abs brush share">SHARE<br>WITH US</div>
  <div class="abs social right" style="left:333px;top:1029px;transform:rotate(-5deg)"><i></i>Tavlora</div>
  <div class="abs social right" style="left:336px;top:1062px;transform:rotate(-2deg)"><i></i>Roamly</div>
  <div class="abs social right" style="left:338px;top:1095px;transform:rotate(4deg)"><i></i>Sketchpit</div>
</section>

<section>
  <div class="abs quote-line"></div>
  <div class="abs brush happy">I Make My Clients Happy!</div>
  <div class="abs mark" style="left:530px;top:938px">&ldquo;</div>
  <p class="abs quote">Lorem ipsum dolor sit amet, consectetur adipisicing elit, sed do eiusmod tempor incididunt ut labore et dolore magna aliqua. Ut enim ad minim veniam, quis nostrud exercitation ullamco laboris nisi ut aliquip ex ea commodo consequat. Duis aute irure dolor in reprehenderit in voluptate velit esse cillum dolore eu fugiat nulla pariatur. Excepteur sint occaecat cupidatat non proident, sunt in culpa qui officia deserunt mollit anim id est laborum.</p>
  <div class="abs mark" style="left:876px;top:1078px">&rdquo;</div>
</section>

<footer class="abs footer">
  <div class="flogo">Karrow<br>Films</div>
  <p>&copy;2011 Karrow Films. All rights reserved.</p>
</footer>
</body>
</html>
```